Brochure Projecct

I need a brochure created for my company, which will be sent to customers via email in PDF format. I have uploaded the company logo with this project, which I want incorporated in the design.

Designers should view the company website at www.brightcounselpages.com. I want the brochure to compliment the website (i.e., very clean design). I would also like pictures added to the brochure to make the design visually stunning.

In terms of content, I need four pages in the brochure to add four separate sections of content (one section per page). The four sections of content will be as follows (1) Search Engine Optimization Benefits (2) Increased Client Retention (3) Showcase Your Law Firm (4) Maximize Your Online ROI (5) Pricing Plans. I will give the content to the winning designer to add to the project. Each individual content section will have four subsection titles after which content of approximately 100 to 200 words will appear.

Designers can decide if other pages should be added to the brochure (i.e., a "cover page" that would have little content, but be visually appealing like the cover of a book - - - a "back page" that may just have the logo, contact information, etc).

My company address and email address should be prominently featured through every page (address: 2715 West Juniper Avenue, Suite 1400, Scottsdale, Arizona 85317; email: sales@brightcounselpages.com).

Industry/Entity Type

It Company

Requirements
Must have
• Clean look but visually stunning incorporating the design of the website at brightcounselpages.com as well as the logo. Also, room for content as set forth in the description of this project.

```html
<!DOCTYPE html>
<html lang="en">
<head>
<meta charset="utf-8">
<title>Bright Counsel Pages – Arizona Legal Services Directory</title>
<link rel="stylesheet" href="https://fonts.googleapis.com/css2?family=Cabin:ital,wght@0,400;0,600;0,700;1,600;1,700&display=swap">
<style>
:root{
  --sky-top:#b9c7e3;
  --sky-mid:#7f98cf;
  --sky-deep:#4f6db3;
  --ink:#1d1d1f;
  --navy:#1f2f6e;
  --brand-blue:#3f6fb8;
  --cyan-panel:#8ec8ea;
  --web-band:#b7def3;
  --url-band:#5a78c4;
  --tile:#ffffff;
  --footer-band:#d9d9d9;
  --logo-border:#9a9a9a;
}
*{box-sizing:border-box;margin:0;padding:0}
html,body{width:1200px;height:851px;overflow:hidden;background:#fff}
ul{list-style:none}
.brochure{position:relative;width:1200px;height:851px;background:#fff;font-family:"Cabin",sans-serif;color:var(--ink)}
.hero{
  position:absolute;left:0;top:0;width:1200px;height:633px;
  background:
    radial-gradient(ellipse 70px 260px at 600px 520px, rgba(255,255,255,.85), rgba(255,255,255,0) 70%),
    radial-gradient(ellipse 420px 200px at 600px 470px, rgba(238,242,251,.6), rgba(238,242,251,0) 70%),
    linear-gradient(180deg,var(--sky-top) 0%,var(--sky-mid) 55%,var(--sky-deep) 100%);
}
.title-panel{position:absolute;left:218px;top:0;width:764px;height:298px;background:rgba(255,255,255,.35)}
.title-panel .accent{position:absolute;left:364px;top:0;width:276px;height:298px;background:var(--cyan-panel);opacity:.85}
.headline{position:absolute;left:355px;top:198px;font-size:29px;font-weight:400;color:var(--ink);white-space:nowrap;letter-spacing:-.2px}
.headline strong{font-weight:700;color:var(--navy)}
.frame{position:absolute;border:1.5px solid rgba(255,255,255,.9)}
.services{position:absolute;left:6px;top:342px;display:flex;gap:4px}
.service{width:96px;height:153px;background:var(--tile);display:flex;flex-direction:column;justify-content:space-between;padding:6px 6px 5px;font-size:12.5px;font-style:italic;font-weight:700;line-height:1.2;color:var(--ink);box-shadow:0 0 0 3px rgba(150,160,175,.55)}
.service .photo{height:58px;margin:4px -6px}
.service .bottom{text-align:right}
.website{position:absolute;left:0;top:684px;width:460px;height:72px;background:var(--web-band);display:flex;align-items:center;padding-left:8px}
.website .label{font-style:italic;font-weight:700;font-size:21px;color:var(--navy);margin-right:8px}
.website .url{font-weight:700;font-size:27px;color:var(--navy)}
.website .url span{background:var(--url-band);color:#fff;padding:0 2px}
.brand-box{position:absolute;left:643px;top:650px;width:550px;height:179px;border:1.5px solid var(--logo-border);background:#fff;display:flex;align-items:center;justify-content:center;gap:18px}
.brand-box .mark{width:74px;height:74px;border-radius:50%;background:var(--brand-blue)}
.brand-box .name{font-size:42px;font-weight:700;color:var(--navy);letter-spacing:-.5px}
.contact-strip{position:absolute;left:0;top:822px;width:1200px;height:29px;background:var(--footer-band);display:flex;align-items:center;justify-content:center;gap:14px;font-size:20.5px;font-style:italic;font-weight:700;color:var(--ink);white-space:nowrap}
</style>
</head>
<body>
<main class="brochure">
  <section class="hero">
    <div class="title-panel"><div class="accent"></div></div>
    <h1 class="headline">Local directory of <strong>arizona legal services</strong></h1>

    <div class="frame" style="left:18px;top:316px;width:96px;height:50px"></div>
    <div class="frame" style="left:112px;top:468px;width:80px;height:72px"></div>
    <div class="frame" style="left:212px;top:302px;width:98px;height:60px"></div>
    <div class="frame" style="left:310px;top:470px;width:98px;height:60px"></div>
    <div class="frame" style="left:410px;top:298px;width:100px;height:56px"></div>
    <div class="frame" style="left:510px;top:474px;width:100px;height:66px"></div>
    <div class="frame" style="left:610px;top:298px;width:98px;height:70px"></div>
    <div class="frame" style="left:706px;top:314px;width:98px;height:48px"></div>
    <div class="frame" style="left:804px;top:470px;width:98px;height:56px"></div>
    <div class="frame" style="left:908px;top:298px;width:98px;height:64px"></div>
    <div class="frame" style="left:1004px;top:314px;width:96px;height:48px"></div>
    <div class="frame" style="left:1098px;top:470px;width:98px;height:64px"></div>

    <ul class="services" aria-label="Practice areas">
      <li class="service"><span>Family</span><div class="photo" role="img" aria-label="Pair of wedding rings" style="background:linear-gradient(135deg,#fff,#e0bd6a,#fff)"></div><span class="bottom">Lawyer</span></li>
      <li class="service"><span>Personal<br>Injury<br>Lawyers</span><div class="photo" role="img" aria-label="Ambulance on the street" style="background:linear-gradient(180deg,#c9ced8,#f1f1f1,#c24a3a)"></div><span></span></li>
      <li class="service"><div class="photo" role="img" aria-label="Social security card and forms" style="background:linear-gradient(135deg,#d8e0ea,#6b89b8)"></div><span>Social<br>Security<br>&amp; Workers<br>comp</span></li>
      <li class="service"><span class="bottom">Business</span><span>Lawyers</span><div class="photo" role="img" aria-label="Signing a business contract" style="background:linear-gradient(135deg,#6b4a30,#c79a6a)"></div></li>
      <li class="service"><span>Taxation</span><div class="photo" role="img" aria-label="Hand writing on tax documents" style="background:linear-gradient(135deg,#a07a4c,#efe4d2)"></div><span class="bottom">Lawyers</span></li>
      <li class="service"><span class="bottom">Real<br>Estate</span><div class="photo" role="img" aria-label="Building under construction" style="background:linear-gradient(180deg,#8fb2da,#b48c6a)"></div><span>Lawyers</span></li>
      <li class="service"><div class="photo" role="img" aria-label="Employment application form" style="background:linear-gradient(135deg,#f4f4f4,#9aa7b8)"></div><span>Employment<br>Lawyers</span></li>
      <li class="service"><span>Mediation<br>Lawyers</span><div class="photo" role="img" aria-label="Scales of justice" style="background:linear-gradient(135deg,#fff,#caa24c,#fff)"></div><span></span></li>
      <li class="service"><span>Estate</span><div class="photo" role="img" aria-label="Estate planning worksheet" style="background:linear-gradient(135deg,#2e6fb3,#dfe9f5)"></div><span>Planning<br>Lawyers</span></li>
      <li class="service"><div class="photo" role="img" aria-label="Bankruptcy folder and gavel" style="background:linear-gradient(135deg,#e8e4de,#8a5a3a)"></div><span>Bankruptcy<br>Lawyers</span><span></span></li>
      <li class="service"><span>Criminal<br>Defence<br>Lawyers</span><div class="photo" role="img" aria-label="Gavel and scales on a desk" style="background:linear-gradient(135deg,#7a4a28,#d7ad7a)"></div></li>
      <li class="service"><div class="photo" role="img" aria-label="Copyright notice and gavel" style="background:linear-gradient(135deg,#5c3a24,#c98d58)"></div><span>Intellectual<br>Property</span><span></span></li>
    </ul>
  </section>

  <div class="website"><span class="label">Website:</span><span class="url"><span>www.brightcounselpages</span>.com</span></div>

  <div class="brand-box" aria-label="Bright Counsel Pages">
    <span class="mark"></span>
    <span class="name">Bright Counsel Pages</span>
  </div>

  <footer class="contact-strip">
    <span class="address">2715 West Juniper Avenue, Suite 1400, Scottsdale, Arizona 85317</span>
    <span class="email">email: sales@brightcounselpages.com</span>
  </footer>
</main>
</body>
</html>
```